Zielgruppe
Wir sind ein Personaldienstleister und vermitteln ausländisches medizinisches Fachpersonal an deutsche Einrichtungen. Unsere Zielgruppe sind Krankenhäuser, Pflegeheime, Ärztehäuser, Praxen, Labore und weitere medizinische Institutionen.
Aufgabenstellung
Wir haben eine Infobroschüre sowie eine PowerPoint Präsentation bereits mit einem groben Design erstellt. Texte und Beispielbilder (Stockmaterial) sind ebenfalls vorhanden, gerne wünschen wir uns auch Eigeninitiative bei der Wahl der Bilder passend zum neuen Design.
Wir wünschen uns ein Redesign mit einem kreativen, einzigartigen Design. Zudem ist uns wichtig, dass unsere Infografiken qualitativ und hochwertig gestaltet werden.
Dieses Projekt ist mit zukünftigen Folgeprojekten verbunden, da wir weitere Präsentationen und Broschüren für andere Zielgruppen benötigen.

```html
<!DOCTYPE html>
<html lang="de">
<head>
<meta charset="utf-8">
<title>Vendara HR – Fachkräfteeinwanderungsgesetz</title>
<link rel="stylesheet" href="https://fonts.googleapis.com/css2?family=Ubuntu:wght@500;700&family=Roboto:wght@400;500&display=swap">
<style>
  :root{
    --canvas:#e4e5e6;
    --ink-black:#0b0b0b;
    --band-gray:#3a3a3a;
    --paper:#f1f1f1;
    --paper-edge:#dcdcdc;
    --teal-dark:#1d4246;
    --teal:#2a8a72;
    --text:#3c3c3c;
    --white:#ffffff;
  }
  *{box-sizing:border-box;margin:0;padding:0}
  html,body{width:1200px;height:856px;overflow:hidden}
  body{background:var(--canvas);font-family:"Roboto",sans-serif;display:flex;align-items:center;justify-content:center}
  .spread{display:flex;width:1160px;height:820px;box-shadow:0 8px 30px rgba(0,0,0,.25)}
  .page{position:relative;width:580px;height:820px;overflow:hidden}

  /* left page */
  .page--intro{background:var(--ink-black);color:var(--white)}
  .intro-head{position:absolute;left:34px;top:36px;right:34px}
  .brand{font-family:"Ubuntu",sans-serif;font-weight:700;font-size:25px;letter-spacing:.5px;color:var(--white)}
  .brand-rule{width:220px;height:2px;background:var(--white);margin:8px 0 10px}
  .intro-title{font-family:"Ubuntu",sans-serif;font-weight:700;font-size:17px;line-height:1.2;margin-bottom:12px}
  .intro-text{font-size:10.5px;line-height:1.45;text-align:justify;color:#e9e9e9}
  .intro-photo{position:absolute;left:0;right:0;bottom:0;height:520px;
    background:radial-gradient(ellipse at 45% 40%,#8a5a2e 0%,#4a2e18 30%,#111 65%),
               linear-gradient(#000,#000);}
  .intro-photo::after{content:"";position:absolute;left:0;right:0;bottom:0;height:160px;
    background:linear-gradient(180deg,rgba(230,230,230,0) 0%,#cfcfcf 55%,#a11c24 92%,#5a0f12 100%);opacity:.85}

  /* right page */
  .page--facts{background:linear-gradient(180deg,var(--paper) 0%,var(--paper-edge) 100%)}
  .facts-banner{position:absolute;left:0;top:0;right:0;height:240px;
    background:linear-gradient(180deg,#2c2c2c 0%,#4a4a4a 72%,#9c9c9c 72%,#cfcfcf 100%)}
  .banner-brand{position:absolute;top:34px;left:330px;display:flex;align-items:center;gap:8px;
    font-family:"Ubuntu",sans-serif;font-weight:700;font-size:16px;color:var(--white)}
  .banner-brand .dot{width:14px;height:14px;border-radius:50%;background:var(--teal)}
  .facts-title{position:absolute;left:190px;top:118px;font-family:"Ubuntu",sans-serif;font-weight:700;font-size:30px;color:var(--white)}

  .facts{position:absolute;top:270px;left:30px;right:26px;display:flex;gap:22px}
  .fact-list{list-style:none;flex:1}
  .fact{position:relative;padding-left:30px;font-size:10.6px;line-height:1.38;color:var(--text);margin-bottom:18px}
  .fact::before{content:"";position:absolute;left:0;top:4px;width:16px;height:16px;border-radius:50%;
    border:2px solid var(--teal-dark);background:radial-gradient(circle,var(--teal-dark) 0 4px,var(--white) 4.5px)}
  .fact:not(:last-child)::after{content:"";position:absolute;left:8px;top:22px;bottom:-16px;border-left:1px dashed #777}

  .facts-footer{position:absolute;left:0;right:0;bottom:0;height:34px;background:var(--teal-dark);
    display:flex;justify-content:space-around;align-items:center;color:var(--white);font-size:10px;letter-spacing:.3px}
</style>
</head>
<body>
<main class="spread">
  <section class="page page--intro">
    <header class="intro-head">
      <div class="brand">Vendara HR</div>
      <div class="brand-rule"></div>
      <h1 class="intro-title">Deutschlands neues<br>Fachkräfteeinwanderungsgesetz<br>für 2023</h1>
      <p class="intro-text">Am 30. November 2022 hat die deutsche Bundesregierung die Eckpunkte des neuen Fachkräfteeinwanderungsgesetztes verabschiedet. Damit will Deutschland massiv die Bildungschancen verbessern, Aus- und Weiterbildung gezielt voranbringen sowie die Einwanderung für Fachkräfte erheblich erleichtern – insbesondere für Personen aus Drittstaaten und somit auch für erwerbstätige Menschen aus der Türkei. Wir haben die wichtigsten Fakten für Sie übersichtlich im Folgenden zusammengefasst.</p>
    </header>
    <div class="intro-photo" role="img" aria-label="Foto: Richterhammer aus Holz auf einem aufgeschlagenen Gesetzbuch vor schwarzem Hintergrund"></div>
  </section>

  <section class="page page--facts">
    <div class="facts-banner" role="img" aria-label="Foto: großes weißes Paragrafenzeichen vor dunkelgrauer Wand">
      <div class="banner-brand"><span class="dot"></span>Vendara HR</div>
      <h2 class="facts-title">Die Fakten im Überblick</h2>
    </div>

    <div class="facts">
      <ul class="fact-list">
        <li class="fact">Menschen aus Drittstaaten mit einem deutschen oder einem in Deutschland anerkannten Abschluss sollen fortan jede qualifizierte Beschäftigung ausüben können. Ein Beispiel: eine als Kauffrau für Büromanagement anerkannte Fachkraft kann auch im Bereich Logistik als Fachkraft beschäftigt werden.</li>
        <li class="fact">Stärkung der Bildungsmigration, indem die Aufnahme einer Berufsausbildung oder eines Studiums erleichtert wird</li>
        <li class="fact">Für die „Blaue Karte EU“ wird die Gehaltsschwelle abgesenkt und somit attraktiver für Berufsanfänger:innen</li>
        <li class="fact">In Zukunft soll ein ausländischer Berufs- oder Hochschulabschluss (mind. 2 Jahre) und eine mindestens zweijährige Berufserfahrung in dem angestrebten (nicht-reglementierten) Beruf für einen Aufenthalt zur Erwerbstätigkeit ausreichen – die formale Anerkennung des ausländischen Berufsabschlusses ist nicht erforderlich</li>
        <li class="fact">Für Fachkräfte aus Drittstaaten besteht die Möglichkeit erst nach der Einreise die Anerkennung ihres ausländischen Berufsabschlusses anerkennen zu lassen und nebenher bereits eine qualifizierte Beschäftigung auszuüben</li>
      </ul>
      <ul class="fact-list">
        <li class="fact">Die Chancenkarte ist neu und richtet sich an qualifizierte Drittstaatsangehörige, die noch keinen Arbeitsvertrag haben. Sie garantiert einen Aufenthaltstitel für bis zu einem Jahr für die Arbeitssuche in Deutschland und berechtigt bereits zu Probe- bzw. Nebenbeschäftigungen</li>
        <li class="fact">Basieren soll die sogenannte Chancenkarte auf Basis eines Punktesystems, ähnlich dem von Kanada. Zu den Auswahlkriterien gehören die QUALIFIKATION, SPRACHKENNTNISSE, BERUFSERFAHRUNG, DEUTSCHLANDBEZUG und das ALTER.</li>
        <li class="fact">Zudem ist die Kurzzeitig befristete Beschäftigungen im Rahmen von Kontingenten geplant, ohne spezielle Qualifikationsanforderungen</li>
        <li class="fact">Die Sprachförderung im In- und Ausland soll deutlich ausgebaut werden</li>
        <li class="fact">Das Anerkennungsverfahren, das Beschleunigte Fachkräfteverfahren sowie das Visumverfahren sollen optimiert und die Bearbeitungszeiten strikter eingehalten werden</li>
        <li class="fact">Erleichterung der Einbürgerung: Die Mindestaufenthaltsdauer soll von 8 auf 5 Jahre herabgesetzt werden, bei besonderen Integrationsleistungen sogar auf 3 Jahre – außerdem muss die alte Staatsbürgerschaft nicht mehr aufgegeben werden</li>
      </ul>
    </div>

    <footer class="facts-footer">
      <span>+49 000 518 27 390</span>
      <span>hr@vendara-hr.de</span>
      <span>www.vendara-hr.de</span>
    </footer>
  </section>
</main>
</body>
</html>
```